Craft Brewery Beer Can Label in Alaska

Design a 16oz can label for a craft brewery.

We are making a can design that can be used for our 6 normal beers. Our desire is to have a standard design but one major element have the color change on each beer type. We included examples of how this works for others.

Elements we general like in designs - mountain scenes, waterfalls, topo map lines, hops. None/all are not required in a design but gives starting options. We are on the ocean in a glacier fjord so think mountains, glaciers and water.

Requirements
Must have
• Company Logo – provided
Frostmark Certified Logo – provided
Freehold Maltsters Logo – provided

Alcohol warning text -

GOVERNMENT WARNING: (1) According to the Surgeon General, women should not drink alcoholic beverages during pregnancy because of the risk of birth defects. (2) Consumption of alcoholic beverages impairs your ability to drive a car or operate machinery, and may cause health problems.

Beer Name – Tide Lantern Pilsner
ABV – 4.9% ABV
Size – 16 FL OZ
Nice to have
• Elements we general like in designs - mountain scenes, waterfalls, topo map lines, hops. None/all are not required in a design but gives starting options. We are on the ocean in a glacier fjord so think mountains, glaciers and water.

```html
<!DOCTYPE html>
<html lang="en">
<head>
<meta charset="utf-8">
<title>Harborline Brewing – Tide Lantern Pilsner Can Labels</title>
<link href="https://fonts.googleapis.com/css2?family=Lobster+Two&family=Montserrat:wght@800&family=Roboto+Condensed:wght@400;700&display=swap" rel="stylesheet">
<style>
  :root{
    --paper:#ffffff;
    --sky-top:#34495a;
    --sky-mid:#5f7588;
    --ice-bright:#e4eaee;
    --ice-shade:#9fb0bd;
    --cave:#2a3a48;
    --water:#14222f;
    --water-glint:#3b556b;
    --silver-light:#f4f5f6;
    --silver-mid:#c3c7ca;
    --silver-dark:#7f8488;
    --ink:#ffffff;
    --blue:#4a86ad;      --blue-deep:#1f2c36;
    --green:#74b83a;     --green-deep:#2f4f1c;
    --orange:#ee8a2c;    --orange-deep:#6e3410;
    --yellow:#f0b535;    --yellow-deep:#5e4410;
    --red:#b8291f;       --red-deep:#6e1812;
    --black:#14191f;     --black-deep:#14191f;
  }
  *{box-sizing:border-box;margin:0;padding:0}
  html,body{width:847px;height:1200px;overflow:hidden;background:var(--paper)}
  .sheet{position:relative;width:847px;height:1200px}

  .label{position:absolute;width:192px;height:456px;overflow:hidden;border-radius:3px;background:var(--water)}
  .label--1{left:68px;top:114px;--accent:var(--blue);--deep:var(--blue-deep)}
  .label--2{left:331px;top:114px;--accent:var(--green);--deep:var(--green-deep)}
  .label--3{left:594px;top:114px;--accent:var(--orange);--deep:var(--orange-deep)}
  .label--4{left:68px;top:706px;--accent:var(--yellow);--deep:var(--yellow-deep)}
  .label--5{left:331px;top:706px;--accent:var(--red);--deep:var(--red-deep)}
  .label--6{left:594px;top:706px;--accent:var(--black);--deep:var(--black-deep)}

  .scene-photo{position:absolute;left:0;top:0;width:192px;height:340px;
    background:linear-gradient(168deg,
      var(--sky-top) 0%, var(--sky-mid) 24%,
      var(--ice-bright) 34%, var(--ice-bright) 44%,
      var(--ice-shade) 52%, var(--cave) 62%,
      var(--water-glint) 70%, var(--water) 80%, var(--water-glint) 88%, var(--water) 100%)}

  .warning{position:absolute;left:4px;top:318px;width:312px;transform-origin:0 0;transform:rotate(-90deg);
    font-family:"Roboto Condensed",sans-serif;font-size:3.7px;line-height:4.6px;color:var(--ink)}

  .beer-name{position:absolute;left:26px;top:12px;font-family:"Lobster Two",cursive;font-weight:400;
    font-size:34px;line-height:44px;color:var(--ink)}
  .style-ribbon{position:absolute;left:26px;top:56px;width:106px;height:13px;background:var(--accent);
    font-family:"Roboto Condensed",sans-serif;font-size:10px;line-height:13px;text-align:center;color:var(--ink);white-space:nowrap}

  .badge-maltsters{position:absolute;left:142px;top:8px;width:38px;height:92px;border:1px solid rgba(255,255,255,.5)}
  .badge-maltsters span{position:absolute;left:14px;top:6px;width:20px;height:80px;background:var(--deep);border-radius:3px}

  .mascot{position:absolute;left:34px;top:216px;width:146px;height:120px;
    background:linear-gradient(180deg,var(--accent),var(--accent) 80%,var(--deep));
    border-radius:46% 54% 10px 10px / 70% 70% 10px 10px}

  .silver-band{position:absolute;left:0;top:333px;width:192px;height:66px;
    background:linear-gradient(90deg,var(--silver-dark),var(--silver-light) 45%,var(--silver-mid) 80%,var(--silver-dark))}
  .swoosh{position:absolute;left:0;top:318px;width:192px;height:28px}

  .wordmark{position:absolute;left:0;top:345px;width:192px;text-align:center;font-family:"Montserrat",sans-serif;font-weight:800;color:var(--deep)}
  .wordmark .w-main{display:block;font-size:25px;line-height:28px}
  .wordmark .w-sub{display:block;font-size:9px;line-height:12px;letter-spacing:11px;padding-left:11px}

  .base-band{position:absolute;left:0;top:386px;width:192px;height:70px}
  .base-info{position:absolute;left:0;top:418px;width:192px;display:flex;align-items:center;justify-content:center;gap:12px;
    font-family:"Roboto Condensed",sans-serif;font-weight:700;font-size:10px;color:var(--ink)}
  .badge-frostmark{display:block;width:30px;height:30px;background:var(--black)}
  .label--6 .badge-frostmark{background:var(--ink)}
</style>
</head>
<body>
<main class="sheet">

  <section class="label label--1">
    <div class="scene-photo" role="img" aria-label="Photograph of a glacier ice wall above a dark fjord with floating ice"></div>
    <p class="warning">GOVERNMENT WARNING: (1) According to the Surgeon General, women should not drink alcoholic beverages during pregnancy because of the risk of birth defects. (2) Consumption of alcoholic beverages impairs your ability to drive a car or operate machinery, and may cause health problems.</p>
    <h2 class="beer-name">Name 1</h2>
    <div class="style-ribbon">Tide Lantern Pilsner</div>
    <div class="badge-maltsters" role="img" aria-label="Freehold Maltsters certification badge"><span></span></div>
    <div class="mascot" role="img" aria-label="Brewery mascot illustration: a sea lion perched on a barrel"></div>
    <div class="silver-band"></div>
    <svg class="swoosh" viewBox="0 0 192 28" preserveAspectRatio="none"><path d="M0 20 Q60 4 192 13 L192 17 Q60 10 0 24Z" fill="var(--accent)"/></svg>
    <div class="wordmark"><span class="w-main">HARBORLINE</span><span class="w-sub">BREWING</span></div>
    <svg class="base-band" viewBox="0 0 192 70" preserveAspectRatio="none"><path d="M0 14 Q90 -4 192 10 L192 70 L0 70Z" fill="var(--accent)"/><path d="M18 22 Q100 6 176 18 Q100 12 18 26Z" fill="#fff"/></svg>
    <div class="base-info"><span>4.9% ABV</span><span class="badge-frostmark" role="img" aria-label="Frostmark Certified badge"></span><span>16 FL OZ</span></div>
  </section>

  <section class="label label--2">
    <div class="scene-photo" role="img" aria-label="Photograph of a glacier ice wall above a dark fjord with floating ice"></div>
    <p class="warning">GOVERNMENT WARNING: (1) According to the Surgeon General, women should not drink alcoholic beverages during pregnancy because of the risk of birth defects. (2) Consumption of alcoholic beverages impairs your ability to drive a car or operate machinery, and may cause health problems.</p>
    <h2 class="beer-name">Name 2</h2>
    <div class="style-ribbon">Tide Lantern Pilsner</div>
    <div class="badge-maltsters" role="img" aria-label="Freehold Maltsters certification badge"><span></span></div>
    <div class="mascot" role="img" aria-label="Brewery mascot illustration: a sea lion perched on a barrel"></div>
    <div class="silver-band"></div>
    <svg class="swoosh" viewBox="0 0 192 28" preserveAspectRatio="none"><path d="M0 20 Q60 4 192 13 L192 17 Q60 10 0 24Z" fill="var(--accent)"/></svg>
    <div class="wordmark"><span class="w-main">HARBORLINE</span><span class="w-sub">BREWING</span></div>
    <svg class="base-band" viewBox="0 0 192 70" preserveAspectRatio="none"><path d="M0 14 Q90 -4 192 10 L192 70 L0 70Z" fill="var(--accent)"/><path d="M18 22 Q100 6 176 18 Q100 12 18 26Z" fill="#fff"/></svg>
    <div class="base-info"><span>4.9% ABV</span><span class="badge-frostmark" role="img" aria-label="Frostmark Certified badge"></span><span>16 FL OZ</span></div>
  </section>

  <section class="label label--3">
    <div class="scene-photo" role="img" aria-label="Photograph of a glacier ice wall above a dark fjord with floating ice"></div>
    <p class="warning">GOVERNMENT WARNING: (1) According to the Surgeon General, women should not drink alcoholic beverages during pregnancy because of the risk of birth defects. (2) Consumption of alcoholic beverages impairs your ability to drive a car or operate machinery, and may cause health problems.</p>
    <h2 class="beer-name">Name 3</h2>
    <div class="style-ribbon">Tide Lantern Pilsner</div>
    <div class="badge-maltsters" role="img" aria-label="Freehold Maltsters certification badge"><span></span></div>
    <div class="mascot" role="img" aria-label="Brewery mascot illustration: a sea lion perched on a barrel"></div>
    <div class="silver-band"></div>
    <svg class="swoosh" viewBox="0 0 192 28" preserveAspectRatio="none"><path d="M0 20 Q60 4 192 13 L192 17 Q60 10 0 24Z" fill="var(--accent)"/></svg>
    <div class="wordmark"><span class="w-main">HARBORLINE</span><span class="w-sub">BREWING</span></div>
    <svg class="base-band" viewBox="0 0 192 70" preserveAspectRatio="none"><path d="M0 14 Q90 -4 192 10 L192 70 L0 70Z" fill="var(--accent)"/><path d="M18 22 Q100 6 176 18 Q100 12 18 26Z" fill="#fff"/></svg>
    <div class="base-info"><span>4.9% ABV</span><span class="badge-frostmark" role="img" aria-label="Frostmark Certified badge"></span><span>16 FL OZ</span></div>
  </section>

  <section class="label label--4">
    <div class="scene-photo" role="img" aria-label="Photograph of a glacier ice wall above a dark fjord with floating ice"></div>
    <p class="warning">GOVERNMENT WARNING: (1) According to the Surgeon General, women should not drink alcoholic beverages during pregnancy because of the risk of birth defects. (2) Consumption of alcoholic beverages impairs your ability to drive a car or operate machinery, and may cause health problems.</p>
    <h2 class="beer-name">Name 4</h2>
    <div class="style-ribbon">Tide Lantern Pilsner</div>
    <div class="badge-maltsters" role="img" aria-label="Freehold Maltsters certification badge"><span></span></div>
    <div class="mascot" role="img" aria-label="Brewery mascot illustration: a sea lion perched on a barrel"></div>
    <div class="silver-band"></div>
    <svg class="swoosh" viewBox="0 0 192 28" preserveAspectRatio="none"><path d="M0 20 Q60 4 192 13 L192 17 Q60 10 0 24Z" fill="var(--accent)"/></svg>
    <div class="wordmark"><span class="w-main">HARBORLINE</span><span class="w-sub">BREWING</span></div>
    <svg class="base-band" viewBox="0 0 192 70" preserveAspectRatio="none"><path d="M0 14 Q90 -4 192 10 L192 70 L0 70Z" fill="var(--accent)"/><path d="M18 22 Q100 6 176 18 Q100 12 18 26Z" fill="#fff"/></svg>
    <div class="base-info"><span>4.9% ABV</span><span class="badge-frostmark" role="img" aria-label="Frostmark Certified badge"></span><span>16 FL OZ</span></div>
  </section>

  <section class="label label--5">
    <div class="scene-photo" role="img" aria-label="Photograph of a glacier ice wall above a dark fjord with floating ice"></div>
    <p class="warning">GOVERNMENT WARNING: (1) According to the Surgeon General, women should not drink alcoholic beverages during pregnancy because of the risk of birth defects. (2) Consumption of alcoholic beverages impairs your ability to drive a car or operate machinery, and may cause health problems.</p>
    <h2 class="beer-name">Name 5</h2>
    <div class="style-ribbon">Tide Lantern Pilsner</div>
    <div class="badge-maltsters" role="img" aria-label="Freehold Maltsters certification badge"><span></span></div>
    <div class="mascot" role="img" aria-label="Brewery mascot illustration: a sea lion perched on a barrel"></div>
    <div class="silver-band"></div>
    <svg class="swoosh" viewBox="0 0 192 28" preserveAspectRatio="none"><path d="M0 20 Q60 4 192 13 L192 17 Q60 10 0 24Z" fill="var(--accent)"/></svg>
    <div class="wordmark"><span class="w-main">HARBORLINE</span><span class="w-sub">BREWING</span></div>
    <svg class="base-band" viewBox="0 0 192 70" preserveAspectRatio="none"><path d="M0 14 Q90 -4 192 10 L192 70 L0 70Z" fill="var(--accent)"/><path d="M18 22 Q100 6 176 18 Q100 12 18 26Z" fill="#fff"/></svg>
    <div class="base-info"><span>4.9% ABV</span><span class="badge-frostmark" role="img" aria-label="Frostmark Certified badge"></span><span>16 FL OZ</span></div>
  </section>

  <section class="label label--6">
    <div class="scene-photo" role="img" aria-label="Photograph of a glacier ice wall above a dark fjord with floating ice"></div>
    <p class="warning">GOVERNMENT WARNING: (1) According to the Surgeon General, women should not drink alcoholic beverages during pregnancy because of the risk of birth defects. (2) Consumption of alcoholic beverages impairs your ability to drive a car or operate machinery, and may cause health problems.</p>
    <h2 class="beer-name">Name 6</h2>
    <div class="style-ribbon">Tide Lantern Pilsner</div>
    <div class="badge-maltsters" role="img" aria-label="Freehold Maltsters certification badge"><span></span></div>
    <div class="mascot" role="img" aria-label="Brewery mascot illustration: a sea lion perched on a barrel"></div>
    <div class="silver-band"></div>
    <svg class="swoosh" viewBox="0 0 192 28" preserveAspectRatio="none"><path d="M0 20 Q60 4 192 13 L192 17 Q60 10 0 24Z" fill="var(--accent)"/></svg>
    <div class="wordmark"><span class="w-main">HARBORLINE</span><span class="w-sub">BREWING</span></div>
    <svg class="base-band" viewBox="0 0 192 70" preserveAspectRatio="none"><path d="M0 14 Q90 -4 192 10 L192 70 L0 70Z" fill="var(--accent)"/><path d="M18 22 Q100 6 176 18 Q100 12 18 26Z" fill="#fff"/></svg>
    <div class="base-info"><span>4.9% ABV</span><span class="badge-frostmark" role="img" aria-label="Frostmark Certified badge"></span><span>16 FL OZ</span></div>
  </section>

</main>
</body>
</html>
```